VornaDerm/The experts in permanent hairremoval

Our Brand is VornaDerm and we are specialized on permantent hair removal for the body for men and woman. VornaDerm is working as a Franchise chain.
The brand should be positioned as lifestyle brand but with a medical background. People should trust in us. We take care about their body. This need to be communicated 100%.
Our system is inexpensive but we don't want to show that we are cheap. So we want to communicate that permanent hair removal is a real lifestyle product but affordable.
We already created a logo that you can see the style and colour we prefer.

Target Market(s)

Europe beginning (especially german spoken markets), Middle East, Africa

Industry/Entity Type

Hair Removal

Number of Pages Required

5+ page

Font styles to use
Serif
Other font styles liked:
• Trajan Pro

Requirements
Nice to have
• We are very open for new ideas

```html
<!DOCTYPE html>
<html lang="en">
<head>
<meta charset="utf-8">
<title>VornaDerm – The Experts in Permanent Hair Removal</title>
<link rel="stylesheet" href="https://fonts.googleapis.com/css2?family=Cinzel:wght@400;700&family=Open+Sans:wght@300;400;600;700&family=Roboto:wght@400;500;700&display=swap">
<style>
  :root {
    --brand-blue: #52aee0;
    --brand-gray: #7a7b80;
    --light-line: #cfe6f4;
    --ink: #222222;
    --white: #ffffff;
    --footer-bg: #333333;
    --footer-base: #262626;
    --footer-text: #e6e6e6;
    --hero-pink: #f6d6d3;
    --skin: #d9a17c;
  }
  * { box-sizing: border-box; margin: 0; padding: 0; }
  html, body { width: 1200px; height: 2299px; overflow: hidden; }
  body {
    position: relative;
    background: var(--white);
    font-family: "Open Sans", Arial, sans-serif;
    color: var(--ink);
  }
  .abs { position: absolute; }
  .shapes { position: absolute; left: 0; top: 0; }

  /* header */
  .social-bar { left: 644px; top: 0; width: 556px; height: 61px; }
  .social-dot { position: absolute; top: 20px; width: 22px; height: 22px; border-radius: 50%; background: var(--white); opacity: .9; }
  .main-nav { left: 470px; top: 92px; display: flex; gap: 0; }
  .main-nav a {
    position: absolute; font-family: "Roboto", Arial, sans-serif; font-size: 15px; font-weight: 500;
    color: var(--ink); text-decoration: none; white-space: nowrap;
  }
  .main-nav a.is-active { color: var(--brand-blue); font-weight: 400; }
  .nav-rule { left: 444px; top: 135px; width: 679px; height: 2px; background: var(--light-line); }

  .photo-legs {
    left: 0; top: 0; width: 470px; height: 620px;
    background: radial-gradient(ellipse at 30% 40%, #f0b9ad 0%, var(--hero-pink) 45%, rgba(255,255,255,0) 78%);
  }
  .photo-man {
    left: 728px; top: 406px; width: 472px; height: 310px;
    background: radial-gradient(ellipse at 55% 60%, var(--skin) 0%, #c98b66 40%, rgba(255,255,255,0) 72%);
  }

  .brand-mark { left: 302px; top: 305px; width: 100px; height: 100px; border-radius: 50%; background: var(--brand-blue); }
  .brand-divider { left: 439px; top: 262px; width: 1px; height: 180px; background: #c9c9cc; }
  .brand-name {
    left: 458px; top: 292px; font-family: "Cinzel", Georgia, serif; font-size: 88px; font-weight: 400;
    color: var(--brand-gray); letter-spacing: 1px; line-height: 1;
  }
  .brand-tagline {
    left: 470px; top: 404px; font-family: "Cinzel", Georgia, serif; font-size: 18px; font-weight: 400;
    color: var(--brand-gray); letter-spacing: .5px; white-space: nowrap;
  }

  /* about */
  .about-title { left: 80px; top: 726px; font-size: 40px; font-weight: 300; color: var(--white); letter-spacing: .5px; }
  .about-text { left: 80px; top: 814px; width: 700px; font-family: "Roboto", Arial, sans-serif; font-size: 16px; line-height: 29px; color: var(--white); }
  .btn-outline {
    left: 77px; top: 970px; width: 177px; height: 51px; border: 1.5px solid var(--white);
    color: var(--white); font-family: "Roboto", Arial, sans-serif; font-size: 17px; display: flex; align-items: center; justify-content: center;
  }
  .photo-woman {
    left: 736px; top: 730px; width: 280px; height: 440px;
    background: radial-gradient(ellipse at 50% 50%, #e8b99a 0%, #dca888 45%, rgba(82,174,224,0) 75%);
  }

  /* appointment card */
  .card-text { left: 40px; top: 1200px; width: 434px; text-align: center; font-size: 21px; line-height: 31px; color: var(--ink); }
  .card-cta { left: 40px; top: 1314px; width: 434px; text-align: center; font-family: "Roboto", Arial, sans-serif; font-size: 24px; font-weight: 500; color: var(--ink); }
  .btn-solid {
    background: var(--brand-blue); color: var(--white); font-family: "Roboto", Arial, sans-serif;
    display: flex; align-items: center; justify-content: center;
  }
  .book-now { left: 146px; top: 1376px; width: 207px; height: 51px; font-size: 20px; font-weight: 500; }

  /* benefits */
  .benefits-title { left: 651px; top: 1200px; font-size: 41px; font-weight: 300; color: var(--white); white-space: nowrap; }
  .benefit-icon { position: absolute; left: 549px; width: 128px; height: 128px; }
  .benefit-heading { left: 699px; font-family: "Cinzel", Georgia, serif; font-size: 27px; color: var(--white); letter-spacing: 1px; }
  .benefit-text { left: 699px; width: 410px; font-size: 16px; line-height: 25px; color: var(--white); }

  /* procedures */
  .procedures-line {
    left: 81px; top: 1856px; width: 790px; font-family: "Cinzel", Georgia, serif; font-size: 33px; line-height: 46px;
    color: var(--brand-blue); letter-spacing: 1px;
  }
  .all-procedures { left: 866px; top: 1882px; width: 254px; height: 57px; font-size: 27px; font-weight: 700; box-shadow: 0 6px 14px rgba(0,0,0,.12); }

  /* footer */
  .site-footer { left: 0; top: 2026px; width: 1200px; height: 230px; background: var(--footer-bg); }
  .footer-base { left: 0; top: 2256px; width: 1200px; height: 43px; background: var(--footer-base); color: var(--footer-text); font-size: 16px; display: flex; align-items: center; justify-content: center; border-top: 1px solid #444; }
  .footer-base strong { color: var(--brand-blue); font-weight: 700; }
  .footer-heading { top: 2040px; font-family: "Cinzel", Georgia, serif; font-size: 29px; color: var(--brand-blue); letter-spacing: 1px; }
  .footer-link { font-size: 16px; color: var(--footer-text); white-space: nowrap; }
  .footer-link.is-active { color: var(--brand-blue); }
  .hours-day { left: 447px; font-size: 16px; font-weight: 700; color: var(--white); }
  .hours-time { left: 624px; font-size: 16px; color: var(--footer-text); }
  .contact-row { left: 808px; font-size: 17px; color: var(--footer-text); display: flex; align-items: center; gap: 8px; white-space: nowrap; }
  .contact-row svg { width: 18px; height: 18px; flex: none; }
</style>
</head>
<body>

<svg class="shapes" width="1200" height="2299" viewBox="0 0 1200 2299" aria-hidden="true">
  <polygon points="0,625 1200,717 1200,1137 0,1223" fill="var(--brand-blue)"/>
  <polygon points="0,1223 1200,1137 1200,1816 0,1724" fill="var(--brand-gray)"/>
  <polygon points="10,1127 500,1108 500,1524 10,1541" fill="rgba(0,0,0,.28)"/>
  <polygon points="0,1119 490,1100 490,1514 0,1533" fill="var(--white)"/>
</svg>

<!-- header -->
<svg class="abs social-bar" viewBox="0 0 556 61" aria-hidden="true">
  <polygon points="0,0 556,0 556,61 28,61" fill="var(--brand-gray)"/>
</svg>
<span class="social-dot" style="left:916px"></span>
<span class="social-dot" style="left:970px"></span>
<span class="social-dot" style="left:1024px"></span>
<span class="social-dot" style="left:1074px"></span>

<nav class="abs main-nav">
  <a class="is-active" style="left:25px">Home</a>
  <a style="left:103px">About</a>
  <a style="left:181px">Studios</a>
  <a style="left:267px">Appoinment</a>
  <a style="left:390px">Carrers</a>
  <a style="left:471px">Feanchise</a>
  <a style="left:570px">Contact Us</a>
</nav>
<div class="abs nav-rule"></div>

<div class="abs photo-legs" role="img" aria-label="Photo of smooth crossed legs with white orchid flowers on a soft pink bokeh background"></div>
<div class="abs photo-man" role="img" aria-label="Photo of a man seen from behind with hands clasped behind his head"></div>

<div class="abs brand-mark"></div>
<div class="abs brand-divider"></div>
<div class="abs brand-name">VornaDerm</div>
<div class="abs brand-tagline">THE EXPERTS IN PERMANENT HAIR REMOVAL</div>

<!-- about -->
<h2 class="abs about-title">ABOUT VORNADERM</h2>
<p class="abs about-text">Lorem ipsum dolor sit amet, consectetur adipiscing elit, sed do eiusmod tempor incididunt ut labore et dolore magna aliqua. Ut enim ad minim veniam, quis nostrud exercitation ullamco laboris nisi ut aliquip ex ea commodo consequat.</p>
<a class="abs btn-outline">READ MORE</a>
<div class="abs photo-woman" role="img" aria-label="Photo of a woman in a white top raising one arm to show a smooth underarm"></div>

<!-- appointment card -->
<p class="abs card-text">People should trust in us. We take care about their body. This need to be communicated 100%.</p>
<p class="abs card-cta">Book your Appointment</p>
<a class="abs btn-solid book-now">Book Now</a>

<!-- benefits -->
<h2 class="abs benefits-title">Why Permanent Epilation</h2>

<svg class="benefit-icon" style="top:1282px" viewBox="0 0 128 128" aria-hidden="true">
  <circle cx="64" cy="64" r="62" fill="var(--white)"/>
  <circle cx="64" cy="64" r="54" fill="none" stroke="var(--brand-gray)" stroke-width="3"/>
  <g fill="none" stroke="var(--brand-blue)" stroke-width="4" stroke-linecap="round">
    <path d="M52 72 C44 64 44 50 52 44 C58 39 70 39 76 44 C84 50 84 64 76 72 L74 80 L54 80 Z"/>
    <line x1="55" y1="86" x2="73" y2="86"/><line x1="57" y1="92" x2="71" y2="92"/>
    <line x1="64" y1="26" x2="64" y2="30"/><line x1="42" y1="34" x2="45" y2="37"/><line x1="86" y1="34" x2="83" y2="37"/>
    <line x1="34" y1="54" x2="38" y2="54"/><line x1="94" y1="54" x2="90" y2="54"/>
  </g>
</svg>
<h3 class="abs benefit-heading" style="top:1280px">The Method</h3>
<p class="abs benefit-text" style="top:1331px">Lorem Ipsum is simply dummy text of the printing and typesetting industry. Lorem Ipsum has been the industry.</p>

<svg class="benefit-icon" style="top:1450px" viewBox="0 0 128 128" aria-hidden="true">
  <circle cx="64" cy="64" r="62" fill="var(--white)"/>
  <circle cx="64" cy="64" r="54" fill="none" stroke="var(--brand-gray)" stroke-width="3"/>
  <g fill="var(--brand-blue)">
    <rect x="34" y="58" width="14" height="32" rx="2"/>
    <path d="M52 60 L64 36 C66 32 72 33 72 38 L70 54 L90 54 C95 54 97 59 95 63 L88 86 C87 89 85 90 82 90 L52 90 Z"/>
  </g>
</svg>
<h3 class="abs benefit-heading" style="top:1447px">The Method</h3>
<p class="abs benefit-text" style="top:1498px">Lorem Ipsum is simply dummy text of the printing and typesetting industry. Lorem Ipsum has been the industry.</p>

<svg class="benefit-icon" style="top:1622px" viewBox="0 0 128 128" aria-hidden="true">
  <circle cx="64" cy="64" r="62" fill="var(--white)"/>
  <circle cx="64" cy="64" r="54" fill="none" stroke="var(--brand-gray)" stroke-width="3"/>
  <g fill="var(--brand-blue)">
    <rect x="55" y="32" width="18" height="16" rx="2"/>
    <rect x="32" y="76" width="18" height="16" rx="2"/>
    <rect x="55" y="76" width="18" height="16" rx="2"/>
    <rect x="78" y="76" width="18" height="16" rx="2"/>
  </g>
  <g fill="none" stroke="var(--brand-blue)" stroke-width="3">
    <path d="M64 48 V76 M41 76 V62 H87 V76"/>
  </g>
</svg>
<h3 class="abs benefit-heading" style="top:1614px">The Method</h3>
<p class="abs benefit-text" style="top:1665px">Lorem Ipsum is simply dummy text of the printing and typesetting industry. Lorem Ipsum has been the industry.</p>

<!-- procedures -->
<p class="abs procedures-line">We provide a complete range of surgical &amp; non-surgical hair removal procedures</p>
<a class="abs btn-solid all-procedures">All Procedures</a>

<!-- footer -->
<footer class="abs site-footer"></footer>
<h4 class="abs footer-heading" style="left:80px">Useful Links</h4>
<span class="abs footer-link is-active" style="left:80px;top:2098px">Home</span>
<span class="abs footer-link" style="left:80px;top:2122px">About</span>
<span class="abs footer-link" style="left:80px;top:2147px">Studios</span>
<span class="abs footer-link" style="left:80px;top:2172px">Book Apoointment</span>
<span class="abs footer-link" style="left:256px;top:2098px">Job</span>
<span class="abs footer-link" style="left:256px;top:2122px">Franchise</span>
<span class="abs footer-link" style="left:256px;top:2147px">Contact</span>

<h4 class="abs footer-heading" style="left:447px">Office Hours</h4>
<span class="abs hours-day" style="top:2098px">Monday to Friday :</span><span class="abs hours-time" style="top:2098px">8am to 7pm</span>
<span class="abs hours-day" style="top:2129px">Saturday :</span><span class="abs hours-time" style="top:2129px">9am to 2pm</span>
<span class="abs hours-day" style="top:2160px">Sunday</span><span class="abs hours-time" style="top:2160px">Closed</span>

<h4 class="abs footer-heading" style="left:812px">Contact Info</h4>
<div class="abs contact-row" style="top:2093px">
  <svg viewBox="0 0 18 18" aria-hidden="true"><path d="M9 1 C5.5 1 3.5 3.5 3.5 6.5 C3.5 10.5 9 17 9 17 C9 17 14.5 10.5 14.5 6.5 C14.5 3.5 12.5 1 9 1 Z" fill="var(--brand-blue)"/><circle cx="9" cy="6.5" r="2" fill="var(--footer-bg)"/></svg>
  <span>Lorem Ipsum is simply dummy text.</span>
</div>
<div class="abs contact-row" style="top:2124px">
  <svg viewBox="0 0 18 18" aria-hidden="true"><path d="M4 1 L7 5 L5.5 7 C6.5 9.5 8.5 11.5 11 12.5 L13 11 L17 14 L15 17 C8 17 1 10 1 3 Z" fill="var(--brand-blue)"/></svg>
  <span>123 456 7890</span>
</div>
<div class="abs contact-row" style="top:2157px">
  <svg viewBox="0 0 18 18" aria-hidden="true"><rect x="1" y="5" width="16" height="11" rx="1.5" fill="var(--brand-blue)"/><rect x="5" y="1" width="8" height="6" fill="var(--brand-blue)"/><rect x="4" y="9" width="10" height="4" fill="var(--footer-bg)"/></svg>
  <span>123 456 7890</span>
</div>
<div class="abs contact-row" style="top:2192px">
  <svg viewBox="0 0 18 18" aria-hidden="true"><rect x="1.5" y="3.5" width="15" height="11" fill="none" stroke="var(--brand-blue)" stroke-width="1.6"/><path d="M1.5 3.5 L9 10 L16.5 3.5" fill="none" stroke="var(--brand-blue)" stroke-width="1.6"/></svg>
  <span>info@vornaderm.example</span>
</div>

<div class="abs footer-base">©&nbsp;<strong>Vorna Derm</strong>&nbsp;- 2015. All Rights Reserved.</div>

</body>
</html>
```